Branding product image: TOMBEL (Golden Papaya) in Plastic Cup (Ready to Eat)

The product is sliced Fruit in Light syrup
Flavour: TOMBEL (Golden Papaya)
The temporary product name: TOMBEL
I want the product design to be something 'fun', 'natural', and 'colourful'
The design concept could be anything depends on your imagination, but it must be eye catchy and attractive.
Basically, I want you to be creative in designing the logo and the overall graphic design for the label.
The measurement is 20 cm (Length) x 6,5 cm (Height)
The target customers are young and health conscious audiences (10 years - 65 years old).
Create something different. Something extraordinary.
Brief summary about the fruit:
This fruit only grows in certain part of the world. It grows in mountain area that is in tropical climate. The fruit flesh has a yellowish-golden color. It has an extraordinary taste (unlike normal papaya) and it suits very well with any dishes from cold appetizer, white/ red meat, desserts, and cocktails.
I need a packaging design for Fruit Cup productThe product is sliced Fruit in Light syrup.There will be various flavours i.e. apple, lychee, peach, papaya, etc.However, you may design the product using one sample flavour (i.e. papaya) first, as the designs of other flavours could be adjusted afterwards.The temporary product name is: RICCANAI want the product design to be something 'fun', 'natural', and 'colourful'.The design concept could be anything depends on your imagination. Basically, I want you to be creative in designing the logo and the overall graphic design for the label. - Create something different. Something extraordinary -Additional:The measurement is 20cm (Length) x 5cm (Height).The target customers are young audiences (10 years - 35 years old).The product design must stand out in the supermarket shelf.It must be eye catchy and attractive.Thank you,Harold-PLEASE REFER TO DESIGN SAMPLE ATTACHED TO HAVE A BETTER UNDERSTANDING FOR THE PRODUCT CONCEPT- Added Wednesday, September 17, 2014
Project Deadline Extended Reason: Haven't found a good design. Added Friday, September 19, 2014
Project Deadline Extended Reason: Need more time for designers to finalize and perfect the design.Thank you,Harold Added Monday, September 29, 2014
Project Deadline Extended Reason: I haven't found a great design yet. Added Tuesday, February 24, 2015
Reason: Getting better designs now. Still Open to new ideas while refining the latest designs from some designers.
Please do your best in submitting other great designs!

```html
<!DOCTYPE html>
<html lang="en">
<head>
<meta charset="utf-8">
<title>LUPEDOS Papaya Fruit Cup Label</title>
<link href="https://fonts.googleapis.com/css2?family=Comfortaa:wght@700&family=Montserrat:wght@600;700&display=swap" rel="stylesheet">
<style>
  :root {
    --bg: #ffffff;
    --label-white: #f7f7f7;
    --label-edge: #e2e2e2;
    --amber: #f29a1a;
    --amber-deep: #d9800e;
    --stripe: #f0640f;
    --red: #ee2a24;
    --flavour: #f47a20;
    --fruit-light: #ff9a3c;
    --fruit-dark: #e8561a;
  }
  html, body {
    margin: 0;
    width: 1200px;
    height: 1000px;
    overflow: hidden;
    background: var(--bg);
  }
  .canvas {
    position: relative;
    width: 1200px;
    height: 1000px;
  }
  .label {
    position: absolute;
    left: 220px;
    top: 290px;
    width: 760px;
    height: 420px;
    background: linear-gradient(90deg, var(--label-edge) 0%, var(--label-white) 25%, #ffffff 50%, var(--label-white) 75%, var(--label-edge) 100%);
    overflow: hidden;
  }
  .label__band {
    position: absolute;
    left: 0;
    top: 0;
    width: 760px;
    height: 130px;
  }
  .brand-name {
    position: absolute;
    left: 0;
    right: 0;
    top: 26px;
    margin: 0;
    text-align: center;
    font-family: 'Comfortaa', sans-serif;
    font-weight: 700;
    font-size: 40px;
    letter-spacing: 2px;
    line-height: 1.2;
    color: #ffffff;
  }
  .fruit-art {
    position: absolute;
    left: 318px;
    top: 132px;
    width: 124px;
    height: 72px;
    border-radius: 40px 40px 10px 10px;
    background: linear-gradient(135deg, var(--fruit-light), var(--fruit-dark));
  }
  .flavour-name {
    position: absolute;
    left: 0;
    right: 0;
    top: 218px;
    margin: 0;
    text-align: center;
    font-family: 'Comfortaa', sans-serif;
    font-weight: 700;
    font-size: 82px;
    letter-spacing: 4px;
    line-height: 1;
    color: var(--flavour);
  }
  .syrup-stripe {
    position: absolute;
    left: 60px;
    right: 60px;
    top: 322px;
    height: 24px;
    background: var(--stripe);
    color: #ffffff;
    font-family: 'Montserrat', sans-serif;
    font-weight: 700;
    font-size: 14px;
    letter-spacing: 1px;
    line-height: 24px;
    text-align: center;
  }
  .net-weight {
    position: absolute;
    left: 0;
    right: 0;
    top: 362px;
    margin: 0;
    text-align: center;
    font-family: 'Montserrat', sans-serif;
    font-weight: 700;
    font-size: 13px;
    letter-spacing: 1px;
    color: var(--red);
  }
</style>
</head>
<body>
  <main class="canvas">
    <section class="label">
      <svg class="label__band" viewBox="0 0 760 130" aria-hidden="true">
        <defs>
          <linearGradient id="bandFill" x1="0" x2="1" y1="0" y2="0">
            <stop offset="0" stop-color="#d9800e"/>
            <stop offset="0.5" stop-color="#f6a126"/>
            <stop offset="1" stop-color="#d9800e"/>
          </linearGradient>
        </defs>
        <polygon points="0,0 760,0 760,18 420,104 392,108 380,120 368,108 340,104 0,18" fill="url(#bandFill)"/>
      </svg>
      <h1 class="brand-name">LUPEDOS</h1>
      <div class="fruit-art" role="img" aria-label="Illustration of halved papaya slices with seeds"></div>
      <h2 class="flavour-name">PAPAYA</h2>
      <div class="syrup-stripe">IN LIGHT SYRUP</div>
      <p class="net-weight">NET WT 6OZ/170G</p>
    </section>
  </main>
</body>
</html>
```